Business Card Revision

Need to redesign my business cards for a new professional look. We are a courier company. You can go to www.qvrunners.com to see what we do. The trucks have an old company name (Sprout) on them but that is the company we are just now
changing the name.

Target Market(s)

Potential clients. We service the automotive, plumbing, printing, air freight industries as well as many others.

Industry/Entity Type

Business

Contact Information for Business Card

QVmotion
20864 Lark Fenmore Parkway
Larkston, KY 40973

Thomas R. Wendall
President

tom@qvrunners.com

Main: (555) 555-0147

```html
<!DOCTYPE html>
<html lang="en">
<head>
<meta charset="utf-8">
<title>QVmotion – Business Card</title>
<link href="https://fonts.googleapis.com/css2?family=Open+Sans:wght@400;700&display=swap" rel="stylesheet">
<style>
  :root {
    --page-bg: #e9e6e1;
    --card-bg: #050607;
    --brand-blue: #2f95d8;
    --brand-blue-soft: #2677b4;
    --brand-green: #4cc25a;
  }
  html, body {
    margin: 0;
    width: 1200px;
    height: 1022px;
    overflow: hidden;
    background: var(--page-bg);
  }
  .card {
    position: absolute;
    left: 100px;
    top: 225px;
    width: 1000px;
    height: 572px;
    border-radius: 30px;
    background: var(--card-bg);
    font-family: "Open Sans", Arial, sans-serif;
    box-shadow: 0 10px 30px rgba(0,0,0,.25);
  }
  .brand {
    position: absolute;
    left: 0;
    top: 0;
    width: 500px;
    height: 572px;
    display: flex;
    align-items: center;
    justify-content: center;
    gap: 18px;
  }
  .brand-square {
    width: 44px;
    height: 44px;
    background: var(--brand-blue);
  }
  .brand-name {
    font-size: 64px;
    font-weight: 700;
    color: var(--brand-green);
    letter-spacing: 1px;
  }
  .divider {
    position: absolute;
    left: 512px;
    top: 150px;
    width: 3px;
    height: 272px;
    background: var(--brand-blue);
  }
  .details {
    position: absolute;
    left: 545px;
    top: 150px;
    width: 430px;
  }
  .person-name {
    margin: 0;
    font-size: 40px;
    line-height: 48px;
    font-weight: 700;
    color: var(--brand-blue);
    white-space: nowrap;
  }
  .person-title {
    margin: 0 0 16px;
    font-size: 24px;
    line-height: 30px;
    color: var(--brand-green);
  }
  .address, .contact {
    margin: 0;
    font-size: 22px;
    line-height: 30px;
    color: var(--brand-blue-soft);
    white-space: nowrap;
  }
  .contact-list {
    list-style: none;
    margin: 0;
    padding: 0;
  }
  .contact {
    display: flex;
    align-items: center;
    gap: 10px;
  }
  .contact svg {
    width: 18px;
    height: 18px;
    flex: none;
  }
</style>
</head>
<body>
  <section class="card">
    <div class="brand">
      <span class="brand-square"></span>
      <span class="brand-name">QVmotion</span>
    </div>
    <div class="divider"></div>
    <div class="details">
      <h1 class="person-name">Thomas R. Wendall</h1>
      <p class="person-title">President</p>
      <p class="address">20864 Lark Fenmore Parkway</p>
      <p class="address">Larkston, KY 40973</p>
      <ul class="contact-list">
        <li class="contact">
          <svg viewBox="0 0 24 24" aria-hidden="true"><path fill="#4cc25a" d="M6.6 10.8a15.1 15.1 0 0 0 6.6 6.6l2.2-2.2a1 1 0 0 1 1-.25 11.4 11.4 0 0 0 3.6.57 1 1 0 0 1 1 1V20a1 1 0 0 1-1 1A17 17 0 0 1 3 4a1 1 0 0 1 1-1h3.5a1 1 0 0 1 1 1c0 1.25.2 2.45.57 3.6a1 1 0 0 1-.25 1z"/></svg>
          (555) 555-0147
        </li>
        <li class="contact">
          <svg viewBox="0 0 24 24" aria-hidden="true"><rect x="2" y="5" width="20" height="14" rx="1.5" fill="none" stroke="#4cc25a" stroke-width="2.2"/><path d="M3 6l9 7 9-7" fill="none" stroke="#4cc25a" stroke-width="2.2"/></svg>
          tom@qvrunners.com
        </li>
        <li class="contact">
          <svg viewBox="0 0 24 24" aria-hidden="true"><circle cx="12" cy="12" r="10" fill="none" stroke="#4cc25a" stroke-width="2"/><ellipse cx="12" cy="12" rx="4.5" ry="10" fill="none" stroke="#4cc25a" stroke-width="2"/><path d="M2 12h20M4 7h16M4 17h16" stroke="#4cc25a" stroke-width="1.6"/></svg>
          www.qvrunners.com
        </li>
      </ul>
    </div>
  </section>
</body>
</html>
```